Lantern Holdings Business Card

We are looking to design new business cards for our company. We have two office locations and would like to have both full addresses on the card. Each address needs two lines for the building name and street address and a line or two for the city, state and zip code. There should be a place for 2-3 phone numbers. The addresses and phone numbers are at the bottom of this description. We also need a place to put our company website and one email address. Our logo is attached.
We would like the card to be two sided. The back of the card should have a blue background with some part of our logo design on it. We would like the full logo on the front of the card as well. The front of the card should have a white background with the blue logo. We are open to listing our addresses on the front or the back of the card. The person who designed our logo gave us an excellent business card idea that we really liked. I have attached a picture of his business card idea so that we can build off of it.
Addresses:
The Marlow Exchange
2214 47th Street NW
Washington, DC 20419
Osprey Harbor Tower
815 Tamsin Boulevard #2207
Miami, FL 33987
Phone Numbers: (202) 555-0148
(202) 555-0193
Website: www.lanternholdings-example.com

```html
<!DOCTYPE html>
<html lang="en">
<head>
<meta charset="utf-8">
<title>Lantern Holdings Business Card</title>
<link href="https://fonts.googleapis.com/css2?family=Crimson+Text:wght@400&display=swap" rel="stylesheet">
<style>
  :root {
    --brand-blue: #2d3382;
    --card-white: #ffffff;
    --backdrop: #e4e5e8;
    --ink-light: #ffffff;
    --text-font: "Crimson Text", Georgia, serif;
  }
  html, body {
    margin: 0;
    padding: 0;
    overflow: hidden;
  }
  body {
    width: 1200px;
    height: 926px;
    background: var(--backdrop);
    font-family: var(--text-font);
    position: relative;
  }
  .card {
    position: absolute;
    left: 250px;
    width: 700px;
    height: 400px;
    box-shadow: 0 6px 18px rgba(0,0,0,0.18);
    overflow: hidden;
  }
  /* Front side */
  .card-front {
    top: 43px;
    background: var(--card-white);
  }
  .front-brand {
    position: absolute;
    left: 0;
    right: 0;
    top: 118px;
    display: flex;
    align-items: center;
    justify-content: center;
    gap: 16px;
  }
  .brand-square {
    width: 46px;
    height: 46px;
    border-radius: 6px;
    background: var(--brand-blue);
  }
  .front-brand .brand-name {
    color: var(--brand-blue);
    font-size: 44px;
    letter-spacing: 0.06em;
    text-transform: uppercase;
    font-weight: 400;
  }
  .front-band {
    position: absolute;
    left: 0;
    right: 0;
    bottom: 0;
    height: 86px;
    background: var(--brand-blue);
    display: flex;
    align-items: center;
    justify-content: center;
  }
  .website {
    color: var(--ink-light);
    font-size: 18px;
    letter-spacing: 0.2em;
  }
  /* Back side */
  .card-back {
    top: 483px;
    background: var(--brand-blue);
    color: var(--ink-light);
  }
  .back-brand {
    position: absolute;
    left: 34px;
    top: 30px;
    display: flex;
    align-items: center;
    gap: 10px;
  }
  .back-brand .brand-square {
    width: 30px;
    height: 30px;
    border-radius: 4px;
    background: var(--ink-light);
  }
  .back-brand .brand-name {
    font-size: 28px;
    letter-spacing: 0.05em;
    text-transform: uppercase;
  }
  .phone-line {
    position: absolute;
    left: 0;
    top: 84px;
    display: flex;
    align-items: center;
    gap: 20px;
  }
  .phone-marker {
    width: 24px;
    height: 8px;
    background: var(--ink-light);
  }
  .phones {
    font-size: 19px;
    letter-spacing: 0.06em;
  }
  .offices {
    position: absolute;
    left: 42px;
    bottom: 48px;
    display: flex;
    gap: 44px;
    font-size: 18px;
    line-height: 1.35;
  }
  .office p { margin: 0; }
  .office-miami { padding-top: 26px; }
</style>
</head>
<body>
  <section class="card card-front">
    <div class="front-brand">
      <span class="brand-square"></span>
      <span class="brand-name">Lantern Holdings</span>
    </div>
    <div class="front-band">
      <span class="website">www.lanternholdings-example.com</span>
    </div>
  </section>

  <section class="card card-back">
    <div class="back-brand">
      <span class="brand-square"></span>
      <span class="brand-name">Lantern Holdings</span>
    </div>
    <div class="phone-line">
      <span class="phone-marker"></span>
      <span class="phones">(202) 555-0148 / (202) 555-0193</span>
    </div>
    <div class="offices">
      <address class="office office-dc" style="font-style:normal">
        <p>The Marlow Exchange</p>
        <p>2214 47th Street NW</p>
        <p>Washington, DC 20419</p>
      </address>
      <address class="office office-miami" style="font-style:normal">
        <p>Osprey Harbor Tower</p>
        <p>815 Tamsin Boulevard #2207</p>
        <p>Miami, FL 33987</p>
      </address>
    </div>
  </section>
</body>
</html>
```